HollowPine Ventures Inc. Business Card Design

My business is custom renovations and homes.I would need to have a new business logo created to go along with my company name. The business card should be of a modern style as this is the market I am focused on. I would need my contact information and website posted on the card. I would also like to list a few of the tasks I conduct on the card (such as: Renovations, Additions, Repairs, New Homes, Design, Consultations). On the reverse of the card I currently have just my logo and my motto, "Shaping A Bold Path". However, I am open to completely changing everything as I am starting a new year and would like to excel further. Any new ideas and suggestions are always welcomed. Thank you.

Target Market(s)

Upscale residential and commercial renovations and builds

Industry/Entity Type

Business

Contact Information for Business Card

I would like the design to be able to be laser cut or burnt onto a wooden business card. I will be creating one option of cards for really loyal customers (wooden) and a second option for the everyday customer (paper).

Font styles to use
Other font styles liked:
• Calibri / anything of mordern taste

Colors
f37122
5c5c5c
474747
ffffff

Requirements
Must have
• I would like the colours of my business to be a sharp orange and grey. I believe this will symbolize a modern style. I am open to other suggestions if this is not suitable for the designers tastes. My contact info as follows:
• Will Marsh
• President
• HollowPine Ventures Inc.
• 555-214-3987
• will@hollowpineventures.example
• I would like my website (currently under construction) hollowpineventures.example on the card aswell.
Nice to have
• Along with a modern logo representing HollowPine, I would like something on the card besides the logo and contact information. Perhaps a small background design. I feel it may be nice to have my services listed on the card (in smaller font on the bottom) Renovations, Additions, Repairs, Design, Consultations.
Should not have
• The business card should not have too many different colors. Should not have rounded corners.

```html
<!DOCTYPE html>
<html lang="en">
<head>
<meta charset="utf-8">
<title>HollowPine Ventures Inc. – Business Card</title>
<link rel="stylesheet" href="https://fonts.googleapis.com/css2?family=Michroma&family=Montserrat:wght@400;500;700&display=swap">
<style>
  :root {
    --orange: #f37122;
    --grey: #5c5c5c;
    --grey-dark: #474747;
    --white: #ffffff;
    --stage: #2e2e2e;
    --text-soft: #6a6a6a;
    --rule-light: #d9d9d9;
  }
  * { box-sizing: border-box; margin: 0; padding: 0; }
  html, body {
    width: 1200px; height: 900px; overflow: hidden;
    background: var(--stage);
  }
  .canvas {
    position: relative; width: 1200px; height: 900px;
    display: flex; flex-direction: column; align-items: center; justify-content: center; gap: 36px;
  }
  .card {
    position: relative; width: 700px; height: 400px;
    overflow: hidden;
    box-shadow: 0 10px 30px rgba(0,0,0,.45);
  }
  .mark-square { display: block; background: var(--orange); flex: none; }

  /* Back side */
  .card-back { background: var(--grey); }
  .card-back .brand-mark {
    position: absolute; left: 0; right: 0; top: 120px;
    display: flex; align-items: center; justify-content: center; gap: 18px;
    font-family: "Montserrat", sans-serif; font-weight: 700; font-size: 64px; line-height: 1;
    color: var(--orange); letter-spacing: 1px;
  }
  .card-back .mark-square { width: 30px; height: 30px; }
  .card-back .motto {
    position: absolute; left: 0; right: 0; top: 262px; text-align: center;
    font-family: "Montserrat", sans-serif; font-weight: 500; font-size: 17px;
    letter-spacing: 1.5px; text-transform: uppercase; color: var(--white);
  }
  .card-back .rule-white {
    position: absolute; left: 0; right: 0; top: 318px; height: 2px; background: var(--rule-light);
  }
  .card-back .band-orange {
    position: absolute; left: 0; right: 0; top: 322px; bottom: 0; background: var(--orange);
    clip-path: polygon(0 0, 100% 0, 100% 35%, 0 100%);
  }

  /* Front side */
  .card-front { background: var(--white); }
  .card-front .brand-mark {
    position: absolute; right: 40px; top: 42px;
    display: flex; align-items: center; gap: 10px;
    font-family: "Montserrat", sans-serif; font-weight: 700; font-size: 40px; line-height: 1;
    color: var(--orange);
  }
  .card-front .mark-square { width: 20px; height: 20px; }
  .rule-orange { position: absolute; height: 2px; background: var(--orange); }
  .rule-top { left: 320px; right: 0; top: 118px; }
  .rule-mid { left: 0; right: 0; top: 246px; }
  .company {
    position: absolute; left: 36px; top: 170px;
    font-family: "Michroma", sans-serif; text-transform: uppercase; line-height: 1.15;
  }
  .company .company-name { font-size: 29px; color: var(--orange); letter-spacing: 1px; }
  .company .company-type { font-size: 19px; color: var(--grey-dark); letter-spacing: 1px; }
  .services {
    position: absolute; left: 520px; top: 132px; list-style: none;
    font-family: "Montserrat", sans-serif; font-size: 14px; color: var(--text-soft); line-height: 18px;
  }
  .services li { display: flex; align-items: center; gap: 12px; }
  .services li::before {
    content: ""; width: 7px; height: 7px; border-radius: 50%; background: var(--orange);
  }
  .person { position: absolute; left: 36px; top: 258px; }
  .person .person-name {
    font-family: "Michroma", sans-serif; font-size: 22px; line-height: 28px; color: var(--orange);
  }
  .person .person-role {
    font-family: "Montserrat", sans-serif; font-size: 14px; line-height: 18px; color: var(--text-soft);
  }
  .contacts {
    position: absolute; left: 36px; top: 310px; list-style: none;
    font-family: "Montserrat", sans-serif; font-size: 13.5px; color: var(--grey-dark); line-height: 18px;
  }
  .contacts li { display: flex; align-items: center; gap: 10px; }
  .contacts svg { width: 11px; height: 11px; fill: var(--orange); flex: none; }
  .contacts .web-domain { color: var(--orange); }
  .card-front .foot-line { position: absolute; left: 0; right: 0; bottom: 20px; height: 2px; background: var(--orange); }
  .card-front .foot-band { position: absolute; left: 0; right: 0; bottom: 0; height: 16px; background: var(--grey); }
</style>
</head>
<body>
<main class="canvas">
  <section class="card card-back" aria-label="Card back">
    <div class="brand-mark"><span class="mark-square"></span><span>HollowPine</span></div>
    <p class="motto">Shaping A Bold Path</p>
    <div class="rule-white"></div>
    <div class="band-orange"></div>
  </section>

  <section class="card card-front" aria-label="Card front">
    <div class="brand-mark"><span class="mark-square"></span><span>HollowPine</span></div>
    <div class="rule-orange rule-top"></div>
    <div class="company">
      <div class="company-name">HollowPine</div>
      <div class="company-type">Ventures Inc.</div>
    </div>
    <ul class="services">
      <li>Renovations</li>
      <li>Additions</li>
      <li>Repairs</li>
      <li>New Homes</li>
      <li>Design</li>
      <li>Consultations</li>
    </ul>
    <div class="rule-orange rule-mid"></div>
    <div class="person">
      <div class="person-name">Will Marsh</div>
      <div class="person-role">President</div>
    </div>
    <ul class="contacts">
      <li><svg viewBox="0 0 24 24" aria-hidden="true"><path d="M6.6 10.8a15 15 0 0 0 6.6 6.6l2.2-2.2c.3-.3.7-.4 1-.2 1.1.4 2.3.6 3.6.6.6 0 1 .4 1 1V20c0 .6-.4 1-1 1C10.6 21 3 13.4 3 4c0-.6.4-1 1-1h3.5c.6 0 1 .4 1 1 0 1.3.2 2.5.6 3.6.1.3 0 .7-.2 1z"/></svg><span>555-214-3987</span></li>
      <li><svg viewBox="0 0 24 24" aria-hidden="true"><path d="M2 5h20v14H2zm2 2v.5l8 5 8-5V7l-8 5z"/></svg><span>will@hollowpineventures.example</span></li>
      <li><svg viewBox="0 0 24 24" aria-hidden="true"><path d="M12 2a10 10 0 1 0 0 20 10 10 0 0 0 0-20zm6.9 6h-3a15 15 0 0 0-1.3-4A8 8 0 0 1 18.9 8zM12 4c.8 1.2 1.5 2.5 1.9 4h-3.8c.4-1.5 1.1-2.8 1.9-4zM4.3 14a8 8 0 0 1 0-4h3.4a16 16 0 0 0 0 4zm.8 2h3a15 15 0 0 0 1.3 4A8 8 0 0 1 5.1 16zm3-8h-3a8 8 0 0 1 4.3-4A15 15 0 0 0 8.1 8zM12 20c-.8-1.2-1.5-2.5-1.9-4h3.8c-.4 1.5-1.1 2.8-1.9 4zm2.3-6H9.7a14 14 0 0 1 0-4h4.6a14 14 0 0 1 0 4zm.3 6a15 15 0 0 0 1.3-4h3a8 8 0 0 1-4.3 4zm1.7-6a16 16 0 0 0 0-4h3.4a8 8 0 0 1 0 4z"/></svg><span>www.<span class="web-domain">hollowpineventures</span>.example</span></li>
    </ul>
    <div class="foot-line"></div>
    <div class="foot-band"></div>
  </section>
</main>
</body>
</html>
```